Oven Cleaning Business owner needs business card design

Hi there,
Would like for a business card to be designed for myself, the owner of a professional oven cleaning business on the Sunshine Coast.
Would like it to look sleek, and modern-ish. Bit creative is encouraged too.
Include following:
Name/title: Corin ter Haghe, Owner
Phone number: 1300 482 916
Email: info@hearthshinecrew.com.au
Website: www.hearthshinecrew.com.au

```html
<!DOCTYPE html>
<html lang="en">
<head>
<meta charset="utf-8">
<title>Hearthshine Crew – Business Card</title>
<link rel="stylesheet" href="https://fonts.googleapis.com/css2?family=Archivo+Black&family=Lato:wght@400;700&display=swap">
<style>
  :root {
    --stage: #2e2e2e;
    --card: #1c1c1c;
    --paper: #ffffff;
    --teal: #1ad6d9;
    --ink: #141414;
    --soft-white: #dcdcdc;
  }
  * { box-sizing: border-box; margin: 0; padding: 0; }
  html, body { width: 1200px; height: 689px; overflow: hidden; }
  body {
    background: var(--stage);
    font-family: "Lato", sans-serif;
    position: relative;
  }
  .card {
    position: absolute;
    top: 190px;
    width: 540px;
    height: 310px;
    border-radius: 22px;
    background: var(--card);
    overflow: hidden;
    box-shadow: 0 18px 40px rgba(0,0,0,.45);
  }
  .card--front { left: 40px; }
  .card--back { left: 620px; }

  .wordmark {
    display: flex;
    align-items: center;
    gap: 14px;
    font-family: "Archivo Black", sans-serif;
    text-transform: uppercase;
    letter-spacing: 1px;
  }
  .wordmark__dot {
    border-radius: 50%;
    background: var(--teal);
    flex: none;
  }
  .card--front .wordmark {
    position: absolute;
    left: 50%; top: 50%;
    transform: translate(-50%, -50%);
    color: #ffffff;
    font-size: 34px;
    white-space: nowrap;
  }
  .card--front .wordmark__dot { width: 58px; height: 58px; }

  .back-art { position: absolute; inset: 0; }
  .card--back .wordmark {
    position: absolute;
    left: 36px; top: 112px;
    flex-direction: column;
    gap: 10px;
    color: var(--ink);
    font-size: 19px;
    text-align: center;
    line-height: 1.1;
    width: 170px;
  }
  .card--back .wordmark__dot { width: 46px; height: 46px; }

  .contact {
    position: absolute;
    right: 24px; top: 92px;
    text-align: right;
    white-space: nowrap;
  }
  .contact__name {
    font-family: "Archivo Black", sans-serif;
    color: var(--soft-white);
    font-size: 18px;
    text-transform: uppercase;
    letter-spacing: .3px;
  }
  .contact__role {
    color: var(--teal);
    font-size: 13px;
    margin-top: 2px;
    margin-bottom: 20px;
  }
  .contact__list { list-style: none; }
  .contact__item {
    display: flex;
    justify-content: flex-end;
    align-items: center;
    gap: 8px;
    color: #ffffff;
    font-size: 13px;
    line-height: 1;
    margin-bottom: 9px;
  }
  .contact__item svg { width: 12px; height: 12px; flex: none; }
</style>
</head>
<body>

<section class="card card--front" aria-label="Card front">
  <div class="wordmark">
    <span class="wordmark__dot"></span>
    <span class="wordmark__name">Hearthshine Crew</span>
  </div>
</section>

<section class="card card--back" aria-label="Card back">
  <svg class="back-art" viewBox="0 0 540 310" preserveAspectRatio="none" aria-hidden="true">
    <path d="M0 0 H262 C296 0 310 55 296 135 C282 210 240 280 202 310 H0 Z" fill="var(--teal)"/>
    <path d="M0 0 H250 C282 0 294 55 281 135 C268 210 226 280 188 310 H0 Z" fill="var(--paper)"/>
  </svg>

  <div class="wordmark">
    <span class="wordmark__dot"></span>
    <span class="wordmark__name">Hearthshine Crew</span>
  </div>

  <div class="contact">
    <p class="contact__name">Corin ter Haghe</p>
    <p class="contact__role">Owner</p>
    <ul class="contact__list">
      <li class="contact__item">1300 482 916
        <svg viewBox="0 0 24 24"><path fill="var(--teal)" d="M6.6 10.8a15 15 0 0 0 6.6 6.6l2.2-2.2a1 1 0 0 1 1-.25 11.4 11.4 0 0 0 3.6.57 1 1 0 0 1 1 1V20a1 1 0 0 1-1 1A17 17 0 0 1 3 4a1 1 0 0 1 1-1h3.5a1 1 0 0 1 1 1c0 1.25.2 2.45.57 3.57a1 1 0 0 1-.25 1z"/></svg>
      </li>
      <li class="contact__item">info@hearthshinecrew.com.au
        <svg viewBox="0 0 24 24"><path fill="var(--teal)" d="M2 5h20v14H2z"/><path d="M2 5l10 8 10-8" fill="none" stroke="var(--card)" stroke-width="2"/></svg>
      </li>
      <li class="contact__item">www.hearthshinecrew.com.au
        <svg viewBox="0 0 24 24"><circle cx="12" cy="12" r="10" fill="var(--teal)"/><path d="M2 12h20M12 2c3 3 3 17 0 20M12 2c-3 3-3 17 0 20" fill="none" stroke="var(--card)" stroke-width="1.6"/></svg>
      </li>
    </ul>
  </div>
</section>

</body>
</html>
```